4x6 Postcard Design Full Color Double Sided

Hello, I am in need of a postcard design. The document with details is attached. And I am writing here also:

To My Dear Colleague,

This week, I want you to do yourself and me a favor, okay?

I want you to ask your boss for a $100,000 per year salary increase. If the answer is no then I want you to “give yourself” a

$10,000 per month pay increase RIGHT NOW!

The opportunity to make 6-7 figures using SIMPLE online systems is exploding right before your eyes. Why aren’t you paying attention? Is It because you don’t have any idea how to earn money online? Or are you intimidated by the thought of it because you’re not tech-savvy?

Throw any negative thoughts out of your mind and let us help you build a $100,000 + yearly income that runs on automatic. We’re not promising a million dollars overnight or that you’ll be able to quit your job tomorrow, BUT if an extra $10,000 per month would help you reach your goals, then you should take action today!

OUR SIMPLE IS SO EASY TO USE, A FIFTH GRADER COULD BE SUCCESSFUL!

We’re so sure you will be successful with our system that we are inviting you to
GET STARTED TODAY FOR FREE!!!

That’s right…for FREE! No credit card is required.

GO SIGN UP NOW:
www.qmvhub.com/joinFREE
Enter Referral ID#

LK-R7859

Free offer expires in 48 hours!!!

Instructions for designers:
I’d like the color scheme to stay consistent with my company’s color scheme. To see the color scheme of Blue Harbor Gain go to www.qmvhub.com
As you are reading the text, please make certain parts of the text be emphasized on the postcard – wherever you feel necessary. When you read it, what would catch your attention? Those parts are the parts I’d like you to emphasize on the card by making them bolder, or a different color, or larger or highlighted.

The postcard is a 4x6 card, double-sided, full color

The text above is for the front side. The back will be the same thing, except in the spot where I have LK-R7859. On the backside it should say: (Use ID# on reverse side)

It’s like you are really only designing a one-sided card because the back side is almost an exact duplicate.

Thank you, you rock! =)

Target Market(s)

work from home seekers / make money online enthusiasts

Font styles to use
Serif

Requirements
Must have
• Color scheme similar to the color scheme at www.qmvhub.com
• The rest of the requirements are attached to the word doc.
• I will also send the logo, but it wouldn't let me upload because the file is too large.
Nice to have
• I really I am looking for something that really looks clean, but attention-grabbing

```html
<!DOCTYPE html>
<html lang="en">
<head>
<meta charset="utf-8">
<title>Blue Harbor Gain Postcard</title>
<link rel="stylesheet" href="https://fonts.googleapis.com/css2?family=Roboto:wght@400;500;700&display=swap">
<style>
:root{
  --backdrop:#000000;
  --card:#f4f7fb;
  --ink:#333840;
  --blue-light:#45abe6;
  --blue:#1a7fd0;
  --blue-deep:#0d4f9c;
  --slate:#4f555e;
  --pill:#3a3d42;
  --white:#ffffff;
}
*{margin:0;padding:0;box-sizing:border-box}
html,body{width:771px;height:1200px;overflow:hidden;background:var(--backdrop)}
body{position:relative;font-family:'Roboto',Arial,sans-serif;color:var(--ink)}
.postcard{position:absolute;left:158px;top:304px;width:455px;height:590px;background:linear-gradient(#fbfcfe,var(--card));overflow:hidden}
.header{position:absolute;left:0;top:0;width:455px;height:62px}
.brand{position:absolute;right:18px;top:22px;color:var(--white);font-weight:700;font-size:15px;display:flex;align-items:center;gap:6px;white-space:nowrap}
.brand-dot{width:10px;height:10px;border-radius:50%;border:2px solid var(--white)}
.greeting{position:absolute;left:26px;top:55px;font-size:10px;font-weight:700}
.intro{position:absolute;left:26px;top:72px;width:415px;font-size:9.6px;line-height:14px}
.headline-band{position:absolute;left:0;top:124px;width:455px;height:42px;background:linear-gradient(var(--blue),var(--blue-deep));color:var(--white);font-weight:700;font-size:17.5px;display:flex;align-items:center;justify-content:center}
.band-shadow{position:absolute;left:20px;width:415px;height:10px;border-radius:50%;background:radial-gradient(ellipse at center,rgba(0,0,0,.35),rgba(0,0,0,0) 70%)}
.body-copy{position:absolute;left:21px;top:185px;width:414px;font-size:9.9px;line-height:15px;text-align:justify}
.body-copy p{text-indent:19px}
.claim-box{position:absolute;left:20px;top:317px;width:415px;height:24px;border:1.5px solid var(--blue-light);font-weight:700;font-size:11px;display:flex;align-items:center;justify-content:center;white-space:nowrap}
.invite{position:absolute;left:0;top:347px;width:455px;text-align:center;font-size:9.8px}
.free-call{position:absolute;left:0;top:366px;width:455px;text-align:center;font-size:15px;font-weight:700;color:var(--blue-light)}
.pill{position:absolute;top:393px;width:193px;height:22px;border-radius:11px;background:var(--pill);color:var(--white);font-size:9.6px;display:flex;align-items:center;justify-content:center}
.pill-free{left:29px}
.pill-card{left:232px}
.signup{position:absolute;left:0;top:423px;width:455px;height:117px;background:linear-gradient(var(--blue),var(--blue-deep));color:var(--white)}
.signup-label{position:absolute;left:59px;top:24px;font-size:12px}
.url-button{position:absolute;left:173px;top:16px;width:221px;height:27px;border-radius:8px;background:linear-gradient(#6cc4f4,var(--blue-light));font-size:12px;display:flex;align-items:center;justify-content:center}
.referral{position:absolute;left:139px;top:65px;width:176px;height:31px;border:1.5px solid var(--white);border-top:none;text-align:center}
.referral::before,.referral::after{content:"";position:absolute;top:0;height:1.5px;width:30px;background:var(--white)}
.referral::before{left:0}.referral::after{right:0}
.referral-label{position:absolute;left:0;top:-8px;width:100%;font-size:12px}
.referral-id{position:absolute;left:0;top:11px;width:100%;font-size:12px;font-weight:700}
.expiry{position:absolute;left:0;top:558px;width:455px;display:flex;justify-content:center;align-items:center;gap:4px;font-size:11px;font-weight:700;color:#555a62}
.expiry-badge{background:var(--blue-light);color:var(--white);padding:3px 8px;border-radius:2px}
</style>
</head>
<body>
<main class="postcard">
  <svg class="header" viewBox="0 0 455 62" aria-hidden="true">
    <rect x="0" y="0" width="455" height="7" fill="#45abe6"/>
    <path d="M0 14 H255 C275 14 282 22 290 32 H0 Z" fill="#4f555e"/>
    <path d="M264 0 H455 V61 H330 C300 61 292 40 280 22 C272 10 268 5 264 0 Z" fill="#1a7fd0"/>
  </svg>
  <div class="brand"><span class="brand-dot"></span>Blue Harbor Gain</div>

  <p class="greeting">To My Dear Colleague,</p>
  <p class="intro">This week, I want you to do yourself and me a favor, okay?<br>I want you to ask your boss for a $100,000 per year salary increase. If the answer is no then I want you to “give yourself” a</p>

  <h1 class="headline-band">$10,000 per month pay increase RIGHT NOW!</h1>
  <div class="band-shadow" style="top:164px"></div>

  <div class="body-copy">
    <p>The opportunity to make 6-7 figures using SIMPLE online systems is exploding right before your eyes. Why aren’t you paying attention? Is It because you don’t have any idea how to earn money online? Or are you intimidated by the thought of it because you’re not tech-savvy?</p>
    <p>Throw any negative thoughts out of your mind and let us help you build a $100,000 + yearly income that runs on automatic. We’re not promising a million dollars overnight or that you’ll be able to quit your job tomorrow, BUT if an extra $10,000 per month would help you reach your goals, then you should take action today!</p>
  </div>

  <div class="claim-box">OUR SIMPLE IS SO EASY TO USE, A FIFTH GRADER COULD BE SUCCESSFUL!</div>
  <p class="invite">We’re so sure you will be successful with our system that we are inviting you to</p>
  <p class="free-call">GET STARTED TODAY FOR FREE!</p>
  <div class="pill pill-free">THAT’S RIGHT…FOR FREE!</div>
  <div class="pill pill-card">NO CREDIT CARD IS REQUIRED</div>

  <section class="signup">
    <p class="signup-label">GO <b>SIGN UP</b> NOW:</p>
    <div class="url-button">www.qmvhub.com/joinFREE</div>
    <div class="referral">
      <p class="referral-label">Enter Referral ID#</p>
      <p class="referral-id">LK-R7859</p>
    </div>
  </section>
  <div class="band-shadow" style="top:538px"></div>

  <p class="expiry">FREE OFFER EXPIRES IN <span class="expiry-badge">48 HOURS!!!</span></p>
</main>
</body>
</html>
```